Corporate Design für Praxis für Ergotherapie
Zielgruppe
Es handelt sich um eine Praxis für Ergotherapie, spezialisiert auf Hausbesuche. Zielgruppe sind erwachsene Patienten.
Aufgabenstellung
Das 'klassische ' Erkennungszeichen der Ergotherapie sind meist die Hände oder auch eine Hand. Mir geht es darum, das im Logo nach Möglichkeit erkennbar ist, das ich meinen Beruf mit Professionalität aber auch sehr viel Empathie umsetze. Für mich ist mein Beruf gleichzeitig Berufung.

```html
<!DOCTYPE html>
<html lang="de">
<head>
<meta charset="utf-8">
<title>Halvorsen Ergotherapie – Geschäftsausstattung</title>
<link rel="stylesheet" href="https://fonts.googleapis.com/css2?family=Arimo:wght@400&family=Yanone+Kaffeesatz:wght@400&display=swap">
<style>
  :root {
    --blue: #0a6bb3;
    --green: #69b544;
    --ink: #1a1a1a;
    --rule: #b5b5b5;
    --frame: #222;
    --paper: #ffffff;
  }
  * { margin: 0; padding: 0; box-sizing: border-box; }
  html, body { width: 1200px; height: 720px; overflow: hidden; background: var(--paper); }
  .canvas { position: relative; width: 1200px; height: 720px; font-family: "Arimo", Arial, sans-serif; color: var(--ink); }

  .sheet { position: absolute; left: 148px; top: 34px; width: 448px; height: 647px; border: 1px solid var(--frame); background: var(--paper); overflow: hidden; }
  .card { position: absolute; left: 694px; width: 328px; height: 197px; border: 1px solid var(--frame); background: var(--paper); overflow: hidden; }
  .card--front { top: 31px; }
  .card--contact { top: 259px; }
  .card--band { top: 481px; }

  .brand { position: absolute; display: flex; flex-direction: column; align-items: center; font-family: "Yanone Kaffeesatz", sans-serif; font-weight: 400; color: var(--green); line-height: 1; transform: translateX(-50%); white-space: nowrap; }
  .brand__dot { width: 16px; height: 16px; border-radius: 50%; background: var(--green); margin-bottom: 6px; }
  .brand__name { font-size: 28px; letter-spacing: 1px; }
  .brand__sub { font-size: 16px; letter-spacing: 1px; margin-top: 2px; }
  .brand--sheet .brand__dot { width: 12px; height: 12px; }
  .brand--sheet .brand__name { font-size: 22px; }
  .brand--sheet .brand__sub { font-size: 13px; }

  .sheet__rule { position: absolute; left: 58px; top: 111px; width: 332px; height: 1.5px; background: var(--green); }
  .fold { position: absolute; left: 0; width: 12px; height: 1px; background: var(--frame); }
  .sender { position: absolute; left: 83px; top: 179px; font-size: 3px; letter-spacing: .1px; text-transform: uppercase; color: var(--ink); white-space: nowrap; }
  .recipient { position: absolute; left: 83px; top: 194px; font-size: 7.6px; line-height: 9.2px; color: var(--ink); }
  .recipient__city { position: absolute; left: 83px; top: 233px; font-size: 9.8px; color: var(--ink); }
  .letter-body { position: absolute; left: 83px; top: 274px; width: 334px; font-size: 7.4px; line-height: 9.2px; color: var(--ink); }
  .letter-body p + p { margin-top: 9.2px; }
  .closing { position: absolute; left: 84px; top: 470px; font-size: 7.6px; line-height: 9.4px; color: var(--ink); }
  .sheet-contact { position: absolute; right: 78px; text-align: right; font-size: 7.4px; line-height: 8.6px; color: var(--ink); white-space: nowrap; }
  .sheet-icon { position: absolute; left: 376px; width: 15px; height: 15px; border-radius: 50%; background: var(--green); display: flex; align-items: center; justify-content: center; }

  .band { position: absolute; left: 0; bottom: 0; width: 100%; height: 21px; background: linear-gradient(90deg, var(--blue), var(--green)); }

  .divider { position: absolute; left: 148px; top: 68px; width: 1.5px; height: 75px; background: var(--rule); }
  .person { position: absolute; left: 169px; top: 56px; font-family: "Yanone Kaffeesatz", sans-serif; color: var(--blue); text-transform: uppercase; white-space: nowrap; }
  .person__name { color: var(--green); font-size: 12.5px; line-height: 12px; }
  .person__role { color: var(--green); font-size: 7px; line-height: 9px; }
  .person__lines { font-size: 7.8px; line-height: 9px; margin-top: 3px; }
  .person__row { display: flex; align-items: center; gap: 4px; margin-left: -12px; }
  .person__row svg { width: 8px; height: 8px; flex: none; }
  .person__group { margin-top: 6px; }
</style>
</head>
<body>
<div class="canvas">

  <section class="sheet" aria-label="Briefbogen">
    <div class="brand brand--sheet" style="left:224px; top:24px;">
      <span class="brand__dot"></span>
      <span class="brand__name">Halvorsen</span>
      <span class="brand__sub">Ergotherapie</span>
    </div>
    <div class="sheet__rule"></div>
    <div class="fold" style="top:189px"></div>
    <div class="fold" style="top:323px"></div>
    <div class="fold" style="top:418px"></div>

    <p class="sender">Halvorsen Ergotherapie, Musterstrasse 12, 12345 Musterhausen</p>
    <p class="recipient">AN<br>Vorname Nachname<br>Musterstrasse 12</p>
    <p class="recipient__city">12345 Musterhausen</p>

    <div class="letter-body">
      <p>Lorem ipsum dolor sit amet, consetetur sadipscing elitr, sed diam nonumy eirmod tempor invidunt ut labore et dolore magna aliquyam erat, sed diam voluptua. At vero eos et accusam et justo duo dolores et ea rebum. Stet clita kasd gubergren, no sea takimata sanctus est Lorem ipsum dolor sit amet. Lorem ipsum dolor sit amet, consetetur sadipscing elitr, sed diam nonumy eirmod tempor invidunt ut labore et dolore magna aliquyam erat, sed diam voluptua. At vero eos et accusam et justo duo dolores et ea rebum. Stet clita kasd gubergren, no sea takimata sanctus est Lorem ipsum dolor sit amet. Lorem ipsum dolor sit amet, consetetur sadipscing elitr, sed diam nonumy eirmod tempor invidunt ut labore et dolore magna aliquyam erat, sed diam voluptua. At vero eos et accusam et justo duo dolores et ea rebum. Stet clita kasd gubergren, no sea takimata sanctus est Lorem ipsum dolor sit amet.</p>
      <p>Duis autem vel eum iriure dolor in hendrerit in vulputate velit esse molestie consequat, vel illum dolore eu feugiat nulla facilisis at vero eros et accumsan et iusto odio dignissim qui blandit praesent luptatum zzril delenit augue duis dolore te feugait nulla facilisi. Lorem ipsum dolor sit amet, consectetuer adipiscing elit, sed diam nonummy nibh euismod tincidunt ut laoreet dolore magna aliquam erat volutpat.</p>
      <p>Ut wisi enim ad minim veniam, quis nostrud exerci tation ullamcorper suscipit lobortis nisl ut aliquip ex ea commodo consequat. Duis autem vel eum iriure dolor in hendrerit in vulputate velit esse molestie consequat, vel illum dolore eu feugiat nulla facilisis at vero eros et accumsan et</p>
    </div>

    <p class="closing">Beste Grüße<br>M.Mustermann</p>

    <p class="sheet-contact" style="top:507px">Musterstrasse 12<br>12345 Musterhausen</p>
    <p class="sheet-contact" style="top:531px">+49 1234 12345678<br>+49 1234 12345678</p>
    <p class="sheet-contact" style="top:553px">email@website.de<br>www.website.de</p>
    <span class="sheet-icon" style="top:503px">
      <svg width="9" height="9" viewBox="0 0 10 10"><path d="M5 1 1 5h1.3v4h2.2V6.5h1V9h2.2V5H9z" fill="var(--blue)"/></svg>
    </span>
    <span class="sheet-icon" style="top:527px">
      <svg width="9" height="9" viewBox="0 0 10 10"><path d="M2 2l6 2.5-2.5 1L4.5 8z" fill="var(--blue)"/></svg>
    </span>
    <span class="sheet-icon" style="top:550px">
      <svg width="9" height="9" viewBox="0 0 10 10"><path d="M1 4c0-1.5 8-1.5 8 0v1H7V4H3v1H1zM2.5 5.5h5L8.5 8h-7z" fill="var(--blue)"/></svg>
    </span>

    <div class="band" role="img" aria-label="Farbband in Blau und Grün"></div>
  </section>

  <section class="card card--front" aria-label="Visitenkarte Vorderseite">
    <div class="brand" style="left:162px; top:58px;">
      <span class="brand__dot"></span>
      <span class="brand__name">Halvorsen</span>
      <span class="brand__sub">Ergotherapie</span>
    </div>
  </section>

  <section class="card card--contact" aria-label="Visitenkarte Rückseite">
    <div class="brand" style="left:85px; top:63px;">
      <span class="brand__dot"></span>
      <span class="brand__name">Halvorsen</span>
      <span class="brand__sub">Ergotherapie</span>
    </div>
    <div class="divider"></div>
    <div class="person">
      <p class="person__name">Vorname Nachname</p>
      <p class="person__role">Position</p>
      <p class="person__lines">Musterstrasse 12<br>12345 Musterhausen</p>
      <div class="person__lines person__group">
        <p class="person__row"><svg viewBox="0 0 10 10"><path d="M1 4c0-1.5 8-1.5 8 0v1H7V4H3v1H1zM2.5 5.5h5L8.5 8h-7z" fill="var(--green)"/></svg>+49 1234 12345678</p>
        <p class="person__row"><svg viewBox="0 0 10 10"><rect x="3" y="1" width="4" height="8" rx="1" fill="none" stroke="var(--green)" stroke-width="1.2"/></svg>+49 1234 12345678</p>
      </div>
      <div class="person__lines person__group">
        <p class="person__row"><svg viewBox="0 0 10 10"><rect x="1.5" y="2.5" width="7" height="5" fill="var(--green)"/><path d="M1.5 2.5 5 5.5 8.5 2.5" fill="none" stroke="#fff" stroke-width=".8"/></svg>email@website.de</p>
        <p class="person__row"><svg viewBox="0 0 10 10"><circle cx="5" cy="5" r="3.6" fill="none" stroke="var(--green)" stroke-width="1"/><path d="M1.4 5h7.2M5 1.4v7.2" stroke="var(--green)" stroke-width=".8"/></svg>www.website.de</p>
      </div>
    </div>
    <div class="band" role="img" aria-label="Farbband in Blau und Grün"></div>
  </section>

  <section class="card card--band" aria-label="Visitenkarte Vorderseite mit Farbband">
    <div class="brand" style="left:149px; top:52px;">
      <span class="brand__dot"></span>
      <span class="brand__name">Halvorsen</span>
      <span class="brand__sub">Ergotherapie</span>
    </div>
    <div class="band" role="img" aria-label="Farbband in Blau und Grün"></div>
  </section>

</div>
</body>
</html>
```